AMAZING FLYERS, POSTCARDS, AND MARKETING!!!! - Northgable Shingle & Eave Works, LLC

This project will be for Northgable Shingle & Eave Works, LLC. The flyers and postcards will be used to saturate the Alaska market with our services, and get our name and logo out there for people to remember. We plan to send the flyers and postcards out in a broad scale (both door to door and mail out). We want to send out flyers to realty and property management businesses to introduce our roofing company, and to advertise our services. We would also like to have another version, or the ability to edit the text of the final product to send out the same materials to residential clients (homeowners) by just changing the text slightly to better fit that market.
We have a logo, but need something put together that we can tri-fold and mail out to potential clients. We are planning to do some postcards as well. We would like the option to mail them or bring them to people in person.
We are a locally owned roofing and repair company in Alaska. We would like something professional that will capture their attention and show the potential of working with our company. I included some detailed information about our company and some pictures below of our work trailer and a before/after on a recent project. I also attached our logo files. Please go through the attached data and let us know what you come up with to stir up the marketing aspect of our company. Thank you for your time and consideration.

Project Deadline Extended
Reason: Allowing additional time for designers to submit/resubmit their flyer/postcard ideas based on inquiries and feedback.

Target Market(s)

1.) Homeowners are the first target market.
2.)Realtors and Property Management companies are the second market

Industry/Entity Type

Marketing

Contact Information for Business Card

Include the logo and contact information for our company. These business cards will be for the Owner, Harold Vemstrup, II.
There is also a Co-Owner, Wanda Vemstrup, so we will need the ability to print business cards for each owner. Need to be able to change the title/name and phone number for Wanda's contact information please. Contact information, license #, and logo information on one side of the card. Please tell the potential client a little about us on the back of the card by utilizing the attached information.

Requirements
Must have
• Pertinent information about our company and listed in the company information attachment. Attention getting details and design work. Professional in appearance and unique to our company to set us above the general advertisers in this industry.
Nice to have
• Something that sets our flyers apart from the ones people get every day. We want to rise above normal with our advertising.
Should not have
• Nothing plain and boring.

```html
<!DOCTYPE html>
<html lang="en">
<head>
<meta charset="utf-8">
<title>Northgable Shingle &amp; Eave Works – Tri-fold Inside</title>
<link rel="stylesheet" href="https://fonts.googleapis.com/css2?family=Open+Sans:ital,wght@0,400;0,600;0,700;1,600;1,700&display=swap">
<style>
  :root {
    --backdrop: #e3e3e3;
    --panel-dark: #2a2829;
    --panel-dark-top: #3a3839;
    --swoosh: #a9a9ab;
    --swoosh-light: #d6d6d8;
    --text-light: #e9e9e9;
    --heading: #ffffff;
    --sky: #c9d6df;
    --shingle: #5c5e62;
    --foliage: #4f6b3a;
  }
  * { box-sizing: border-box; margin: 0; padding: 0; }
  html, body {
    width: 1200px; height: 870px; overflow: hidden;
    background: var(--backdrop);
    font-family: "Open Sans", Arial, sans-serif;
  }
  .trifold {
    position: absolute; left: 30px; top: 40px;
    width: 1140px; height: 790px;
    display: flex;
    box-shadow: 0 6px 18px rgba(0,0,0,.25);
  }
  .panel {
    position: relative; width: 380px; height: 790px;
    background: linear-gradient(180deg, var(--panel-dark-top), var(--panel-dark) 60%);
    color: var(--text-light);
    overflow: hidden;
  }
  .panel + .panel { border-left: 1px solid rgba(0,0,0,.35); }
  .panel-art { position: absolute; inset: 0; width: 380px; height: 790px; }
  .panel-copy { position: absolute; left: 30px; right: 30px; }
  .panel-heading {
    color: var(--heading); font-weight: 700; text-transform: uppercase;
    font-size: 18px; line-height: 1.2; letter-spacing: .2px; margin-bottom: 14px;
  }
  .body-text { font-size: 12.2px; line-height: 1.42; text-align: justify; }
  .body-text + .body-text { margin-top: 13px; }
  .feature-list { list-style: none; }
  .feature-list li {
    position: relative; padding-left: 24px; font-size: 15.5px; line-height: 1.25; margin-bottom: 6px;
  }
  .feature-list li::before {
    content: "›"; position: absolute; left: 0; top: 2px;
    width: 14px; height: 14px; border-radius: 50%;
    background: var(--text-light); color: var(--panel-dark);
    font-size: 13px; font-weight: 700; line-height: 12px; text-align: center;
  }
  .intro { top: 36px; }
  .business-copy { top: 640px; }
  .business-copy .panel-heading { margin-bottom: 6px; font-size: 17px; }
  .business-copy .body-text { font-size: 13px; text-align: left; }
  .company-copy { top: 262px; }
  .homeowner-copy { top: 30px; }
  .tagline {
    position: absolute; right: 30px; top: 548px; text-align: right;
    font-style: italic; font-weight: 700; font-size: 18px; line-height: 1.25; color: var(--heading);
  }
</style>
</head>
<body>
<main class="trifold">

  <!-- Panel 1 -->
  <section class="panel panel-business">
    <svg class="panel-art" viewBox="0 0 380 790" aria-hidden="false">
      <defs>
        <linearGradient id="housePhoto" x1="0" y1="0" x2="0" y2="1">
          <stop offset="0" stop-color="#b9c8d4"/>
          <stop offset=".35" stop-color="#6f7a6a"/>
          <stop offset=".7" stop-color="#8e9194"/>
          <stop offset="1" stop-color="#4e6a3a"/>
        </linearGradient>
        <linearGradient id="insetPhoto" x1="0" y1="0" x2="0" y2="1">
          <stop offset="0" stop-color="#c3d2dc"/>
          <stop offset=".5" stop-color="#9d8a78"/>
          <stop offset="1" stop-color="#6b7a5a"/>
        </linearGradient>
      </defs>
      <path d="M0,238 C120,262 250,196 380,206 L380,212 C250,204 120,270 0,248 Z" fill="var(--swoosh-light)"/>
      <path role="img" aria-label="Photo of a finished house roof with garage"
            d="M0,250 C120,272 250,206 380,214 L380,522 C260,556 120,566 0,616 Z" fill="url(#housePhoto)"/>
      <path d="M0,616 C120,566 260,556 380,522 L380,540 C260,572 120,584 0,636 Z" fill="var(--swoosh)"/>
      <rect x="232" y="452" width="134" height="88" fill="#ffffff"/>
      <rect role="img" aria-label="Small photo of the same house before the work" x="237" y="457" width="124" height="78" fill="url(#insetPhoto)"/>
    </svg>
    <div class="panel-copy intro">
      <h1 class="panel-heading">Northgable Shingle &amp; Eave Works</h1>
      <ul class="feature-list">
        <li>Locally owned and operated</li>
        <li>Over two decades in the roofing and repair industry</li>
        <li>Licensed</li>
        <li>Bonded</li>
        <li>Insured</li>
      </ul>
    </div>
    <div class="panel-copy business-copy">
      <h2 class="panel-heading">Background Information<br>for Businesses</h2>
      <p class="body-text">We’ve been working in the nearby area and would like to introduce ourselves. Northgable Shingle &amp; Eave Works, LLC is a local business, owned and operated by people born and raised right here in Alaska.</p>
    </div>
  </section>

  <!-- Panel 2 -->
  <section class="panel panel-company">
    <svg class="panel-art" viewBox="0 0 380 790">
      <defs>
        <linearGradient id="roofPhoto" x1="0" y1="0" x2="1" y2="1">
          <stop offset="0" stop-color="#5f7a4a"/>
          <stop offset=".3" stop-color="#6c6e72"/>
          <stop offset="1" stop-color="#4a4c50"/>
        </linearGradient>
        <linearGradient id="workerPhoto" x1="0" y1="0" x2="1" y2="1">
          <stop offset="0" stop-color="#8a9a98"/>
          <stop offset=".5" stop-color="#a9b8b5"/>
          <stop offset="1" stop-color="#5a5c60"/>
        </linearGradient>
      </defs>
      <path role="img" aria-label="Photo of a new shingle roof under blue sky"
            d="M0,0 H380 V196 C250,168 120,206 0,258 Z" fill="url(#roofPhoto)"/>
      <path d="M0,258 C120,206 250,168 380,196 L380,214 C250,188 120,224 0,272 Z" fill="var(--swoosh)"/>
      <path d="M0,628 C130,598 260,612 380,590 L380,606 C260,626 130,614 0,646 Z" fill="var(--swoosh-light)"/>
      <path role="img" aria-label="Photo of a roofer nailing shingles with a nail gun"
            d="M0,646 C130,614 260,626 380,606 V790 H0 Z" fill="url(#workerPhoto)"/>
    </svg>
    <div class="panel-copy company-copy">
      <p class="body-text">We love our state and the sense of community that is uniquely Alaskan, and strive to give our clients the best service possible. With over two decades of experience in the roofing and repair industry, we would appreciate the opportunity to interview to be your roofing company of choice. Our focus is on quality work for residential client and property management companies, and finding the right service that will best fit their needs.</p>
      <p class="body-text">We offer free estimates for small repairs as well as full roof replacements, and would be happy to assist you if you would like to contact us with any questions.</p>
      <p class="body-text">Our goal is to be Alaska’s premier residential roofing and repair company, and provide quality workmanship to our friends and neighbors.</p>
    </div>
  </section>

  <!-- Panel 3 -->
  <section class="panel panel-homeowners">
    <svg class="panel-art" viewBox="0 0 380 790">
      <defs>
        <linearGradient id="shinglePhoto" x1="0" y1="0" x2="1" y2="1">
          <stop offset="0" stop-color="#6a6c70"/>
          <stop offset=".6" stop-color="#8b8d91"/>
          <stop offset="1" stop-color="#a3a5a8"/>
        </linearGradient>
      </defs>
      <path d="M0,740 C150,720 290,664 380,598 L380,620 C290,684 150,742 0,760 Z" fill="var(--swoosh-light)"/>
      <path role="img" aria-label="Close-up photo of roof shingles along a ridge"
            d="M0,760 C150,742 290,684 380,620 V790 H0 Z" fill="url(#shinglePhoto)"/>
    </svg>
    <div class="panel-copy homeowner-copy">
      <h2 class="panel-heading">Background Information<br>for Homeowners</h2>
      <p class="body-text">We’ve been working in the nearby area and would like to introduce ourselves to your neighborhood. Northgable Shingle &amp; Eave Works, LLC is a local business, owned and operated by people born and raised right here in Alaska. We love our state and the sense of community that is uniquely Alaskan, and strive to give you the best service possible.</p>
      <p class="body-text">With over two decades of experience in the roofing and repair industry, we would appreciate the opportunity to interview to be your roofing company of choice. Our focus is on quality work for the residential homeowner, and finding the right service that will best fit your needs.</p>
      <p class="body-text">We offer free estimates for small repairs as well as full roof replacements, and would be happy to assist you if you would like to contact us with any questions.</p>
      <p class="body-text">Our goal is to be Alaska’s premier roofing and repair company, and provide quality workmanship to our friends and neighbors.</p>
      <p class="body-text">Thank you for your time and have a wonderful day!</p>
    </div>
    <p class="tagline">Giving peace of mind to Alaskans,<br>one roof at a time.</p>
  </section>

</main>
</body>
</html>
```